Hockey Youth Club - Complete HP Design

I need a complete homepage design for a new youth hockey club. There are already some elements that can be used. For more information, please visit this products webpage. This site is currently unavailable for purchase at this time (Current) -) Team (Players, Coaches, Crew) -) Club (Philiosophy , Rules, Management Board, ....) -) Partners (Sponsors, Partners, ...)) Contact (Contact details, Callback Button) -) Shop (in the beginning view of products - further planned as online shop ) -) .... probably 2-3 more -) Footer with social media info, ..... Homepages from other youth hockey clubs (ex. Www.plo. At - this is what I am looking for in my life - BUT we dont want to copy them !!! Im interested in new and innovative designs.
Updates

Project Deadline Extended
Reason: Too much Wordpress - no innovation - please offer more designs in dark concept. At the moment the design is too decent - we are looking for sporty, active and fresh design. Thank you

Target Market(s)

Youth Hockey Players Parents

Industry/Entity Type

Club

Number of Pages Required

5+ page

Colors
fbed38
9d9d9d
1b1b1b
f5f5f5
ffffff

Requirements
Must have
• Clearline, modern design,
Nice to have
• Flashing elements (maybe the scratches fading in ...)
Should not have
• chaos

```html
<!DOCTYPE html>
<html lang="en">
<head>
<meta charset="utf-8">
<title>Stags Youth Hockey Club</title>
<link href="https://fonts.googleapis.com/css2?family=Cinzel:wght@400;700&family=Roboto:wght@400;700&display=swap" rel="stylesheet">
<style>
:root{
  --yellow:#fbed38;
  --gold:#f5c518;
  --grey:#9d9d9d;
  --dark:#1b1b1b;
  --light:#f5f5f5;
  --white:#ffffff;
  --char:#2e2e2e;
  --text:#555;
}
*{margin:0;padding:0;box-sizing:border-box}
html,body{width:1200px;height:5042px;overflow:hidden}
body{position:relative;background:var(--white);font-family:'Roboto',Arial,sans-serif;color:var(--text);font-size:13px}
.abs{position:absolute}
.serif{font-family:'Cinzel',Georgia,serif}
.section-title{position:absolute;left:0;width:1200px;text-align:center;font-family:'Cinzel',Georgia,serif;font-size:30px;font-weight:400;line-height:44px;color:#222;letter-spacing:1px;white-space:nowrap}
.section-title .hl{color:var(--gold)}
.intro{position:absolute;left:120px;width:960px;text-align:center;font-size:12px;line-height:19px;color:#666}
.btn{position:absolute;background:var(--gold);color:#222;font-size:13px;text-align:center;border:none}

/* hero */
.hero{position:absolute;left:0;top:0;width:1200px;height:585px;background:linear-gradient(180deg,#1d2d4a 0%,#2b3f56 45%,#2f5a2a 75%,#173516 100%)}
.hero-photo{position:absolute;left:330px;top:0;width:440px;height:585px;background:radial-gradient(ellipse at center,rgba(200,40,40,.55) 0%,rgba(120,30,30,.25) 40%,rgba(0,0,0,0) 70%)}
.logo-tab{position:absolute;left:0;top:0}
.brand{position:absolute;left:40px;top:30px;font-family:'Cinzel',Georgia,serif;font-weight:700;font-size:40px;color:var(--dark)}
.nav{position:absolute;top:40px;right:40px;display:flex;gap:6px}
.nav a{color:var(--white);text-decoration:none;font-size:13px;padding:6px 10px}
.nav a.active{background:var(--gold);color:#222}
.login{position:absolute;right:50px;top:114px;color:var(--white);font-size:12px}
.tagline{position:absolute;left:760px;top:312px;font-family:'Cinzel',Georgia,serif;font-size:34px;color:var(--white);white-space:nowrap}
.tagline span{color:var(--yellow)}
.subline{position:absolute;left:830px;top:374px;font-family:'Cinzel',Georgia,serif;font-size:20px;color:var(--white);white-space:nowrap}
.subline span{color:var(--yellow)}
.dots{position:absolute;left:583px;top:505px;display:flex;gap:10px}
.dots i{width:12px;height:12px;border-radius:50%;background:#bbb;display:block}
.dots i:first-child{background:var(--white)}

/* results */
.results-frame{position:absolute;left:94px;top:662px;width:1011px;height:386px;border:2px solid var(--gold)}
.results-title span.bg{background:var(--white);padding:0 18px}
.score-band{position:absolute;left:0;top:820px;width:1200px;height:60px;background:#ececec}
.team{position:absolute;top:836px;font-size:26px;color:#333;font-family:'Cinzel',Georgia,serif}
.score{position:absolute;left:555px;top:826px;width:90px;height:48px;background:var(--gold);display:flex;align-items:center;justify-content:space-between;padding:0 12px;font-size:24px;color:#222}
.score i{position:absolute;left:33px;top:12px;width:24px;height:24px;border-radius:50%;background:var(--dark)}

/* about */
.about{position:absolute;left:0;top:1119px;width:1200px;height:437px;background:#262626}
.about-text{position:absolute;left:14px;width:600px;font-size:12px;line-height:18px;color:#3a2e00}
.trainer-photo{position:absolute;left:860px;top:148px;width:232px;height:211px;background:linear-gradient(160deg,#6b5a4a,#2c2420);border:3px solid #666}

/* club */
.club{position:absolute;left:100px;top:1630px;width:999px;height:360px;background:linear-gradient(135deg,#3c3c3c,#2a2a2a)}
.club-frame{position:absolute;left:61px;top:67px;width:891px;height:252px;border:2px solid var(--gold)}
.club-text{position:absolute;left:118px;top:118px;width:770px;font-size:12px;line-height:26px;color:var(--white)}

/* news */
.news-band{position:absolute;left:0;top:2292px;width:1200px;height:322px;background:linear-gradient(180deg,#2c3a2c,#1f4a1e 60%,#2e6a2a)}
.news-img{position:absolute;top:2298px;width:265px;height:178px;background:linear-gradient(180deg,#8aa5b8,#3f6d35)}
.news-card{position:absolute;top:2298px;width:280px;height:178px;background:var(--white);padding:10px 12px;text-align:center}
.news-card .date{font-size:10px;color:#888;text-align:right}
.news-card h3{font-size:15px;font-weight:400;color:#222;margin:6px 0 8px}
.news-card p{font-size:10px;line-height:14px;color:#666}
.news-card .more{position:absolute;left:0;right:0;bottom:10px;font-size:11px;color:#222}

/* team */
.team-band{position:absolute;left:0;top:2933px;width:1200px;height:309px;background:linear-gradient(180deg,#27303a,#1d3a1f)}
.player{position:absolute;top:2940px;height:245px;background:linear-gradient(180deg,#6d6d6d,#3a3a3a)}
.player .num{position:absolute;left:0;top:0;width:44px;height:30px;background:var(--gold);color:#222;font-size:15px;text-align:center;line-height:30px}
.player-name{position:absolute;top:3196px;color:var(--white);font-size:13px;text-align:center}

/* shop */
.shop-band{position:absolute;left:0;top:3602px;width:1200px;height:407px;background:linear-gradient(180deg,#161616,#2a2a2a)}
.promo{position:absolute;left:319px;top:3602px;width:538px;height:44px;background:#000;color:var(--yellow);font-size:20px;text-align:center;line-height:44px}
.product{position:absolute;top:3670px;width:191px;height:228px;background:var(--white)}
.product .jersey{position:absolute;left:16px;top:12px;width:159px;height:162px;background:linear-gradient(180deg,#3a3a3a,#1b1b1b)}
.product .jersey.light{background:linear-gradient(180deg,#f0f0f0,#c9c9c9)}
.product .strip{position:absolute;left:0;bottom:0;width:191px;height:44px;background:var(--dark)}
.product .price{position:absolute;left:10px;bottom:12px;width:70px;height:22px;background:#e9e9e9;color:#333;font-size:12px;text-align:center;line-height:22px}
.product .buy{position:absolute;right:10px;bottom:12px;width:80px;height:22px;background:var(--gold);color:#222;font-size:12px;text-align:center;line-height:22px}

/* contact */
.map{position:absolute;left:0;top:4009px;width:690px;height:551px;background:linear-gradient(135deg,#cfe3f2,#8fb6d8)}
.contact-side{position:absolute;left:690px;top:4009px;width:510px;height:551px;background:#efefef}
.pin-label{position:absolute;height:24px;background:var(--gold);color:#222;font-size:11px;line-height:24px;padding:0 12px 0 28px;white-space:nowrap}
.pin-label i{position:absolute;left:8px;top:6px;width:12px;height:12px;border-radius:50% 50% 50% 0;background:var(--dark);transform:rotate(-45deg)}
.field{position:absolute;left:702px;width:424px;background:var(--white);border:1px solid var(--gold);font-size:13px;color:#333;padding:14px 12px}

/* footer */
.footer{position:absolute;left:0;top:4560px;width:1200px;height:482px;background:#1f1f1f}
.social{position:absolute;top:100px;left:680px;display:flex;gap:28px}
.social i{width:26px;height:26px;border-radius:50%;background:#bdbdbd;display:block}
.bottom-bar{position:absolute;left:0;top:400px;width:1200px;height:82px;background:#141414}
.bottom-nav{position:absolute;left:30px;top:30px;display:flex;gap:26px}
.bottom-nav a{color:var(--white);font-size:12px;text-decoration:none}
</style>
</head>
<body>

<!-- HERO -->
<header class="hero">
  <div class="hero-photo" role="img" aria-label="Young player in red kit celebrating on a floodlit pitch"></div>
  <svg class="logo-tab" width="330" height="140" viewBox="0 0 330 140"><polygon points="0,0 330,0 250,140 0,140" fill="#f5c518"/></svg>
  <div class="brand">Stags</div>
  <nav class="nav">
    <a class="active">HOME</a><a>NEWS</a><a>TEAM</a><a>CLUB</a><a>PARTNER</a><a>SHOP</a><a>CONTACT</a>
  </nav>
  <div class="login">&#9679; REGISTER / LOGIN</div>
  <div class="tagline">LIFE IS <span>ABOUT TIMING</span></div>
  <div class="subline"><span>Have Fun</span> : Enjoy the Game !</div>
  <div class="dots"><i></i><i></i><i></i></div>
  <div class="btn" style="left:1012px;top:522px;width:76px;height:24px;line-height:24px;font-size:11px">READ MORE</div>
</header>

<!-- RESULTS -->
<section>
  <div class="results-frame"></div>
  <h2 class="section-title results-title" style="top:640px;font-size:26px"><span class="bg">LATEST <span class="hl">RESULTS</span></span></h2>
  <div class="abs serif" style="left:0;width:1200px;top:696px;text-align:center;font-size:20px;color:#333">Match Semifinal</div>
  <div class="abs" style="left:0;width:1200px;top:756px;text-align:center;font-size:12px;color:#777">March 3rd, 2017</div>
  <div class="abs" style="left:0;width:1200px;top:794px;text-align:center;font-size:15px;color:#333">score</div>
  <div class="score-band"></div>
  <svg class="abs" style="left:138px;top:826px" width="62" height="48"><rect x="4" y="4" width="54" height="40" rx="6" fill="#d6a21a"/></svg>
  <div class="team" style="left:334px">TEAM 1</div>
  <div class="score">3<i></i>2</div>
  <div class="team" style="left:770px">TEAM 2</div>
  <svg class="abs" style="left:1016px;top:826px" width="50" height="50"><circle cx="25" cy="25" r="24" fill="#3a7cc2"/></svg>
  <p class="intro" style="top:922px;font-size:11px;line-height:17px">Our juniors fought hard through three full periods and earned their place in the final with a late goal and strong defence.<br>Well done to every player, coach and parent who cheered from the stands all night long.</p>
  <div class="btn" style="left:527px;top:992px;width:146px;height:30px;line-height:30px">More Info</div>
</section>

<!-- ABOUT + TRAINERS -->
<section class="about">
  <svg class="abs" style="left:0;top:0" width="800" height="437" viewBox="0 0 800 437"><polygon points="0,0 800,0 460,437 0,437" fill="#f5c518"/></svg>
  <h2 class="abs serif" style="left:192px;top:62px;font-size:30px;font-weight:400;color:#222;white-space:nowrap">ABOUT <span style="color:var(--white)">TEAM</span></h2>
  <p class="about-text" style="top:132px">Our club gives young players a safe place to learn the game, build skills and make friends. Training runs through the whole season for every age group, with coaches who focus on effort, fair play and fun. New players are always welcome to join a trial session and meet the team on the ice.</p>
  <p class="about-text" style="top:270px;width:440px">Parents can follow schedules, results and events here, and our volunteers help at every home game. We believe strong teams grow from good habits both on and off the ice.</p>
  <svg class="abs" style="left:830px;top:112px" width="46" height="28"><polygon points="10,0 46,0 36,28 0,28" fill="#f5c518"/></svg>
  <h2 class="abs serif" style="left:900px;top:110px;font-size:26px;font-weight:400;color:var(--white)">TRAINERS</h2>
  <div class="abs serif" style="left:695px;top:282px;font-size:18px;color:var(--white);white-space:nowrap">Main <span style="color:var(--gold)">Trainer</span></div>
  <div class="trainer-photo" role="img" aria-label="Portrait of the club's head trainer"></div>
</section>

<!-- CLUB -->
<section class="club" role="region" aria-label="Our club">
  <div class="club-frame"></div>
  <h2 class="abs serif" style="left:0;width:999px;top:50px;text-align:center;font-size:28px;font-weight:400;line-height:36px;color:var(--white)"><span style="background:#363636;padding:0 14px">OUR <span style="color:var(--gold)">CLUB</span></span></h2>
  <p class="club-text">Founded by parents and former players, our club welcomes children of every level and background. Training sessions teach skating, passing and teamwork, and each season closes with a family tournament. Our board meets monthly to plan events, review rules and support coaches. Volunteers keep the club running and every helping hand is truly valued.</p>
  <div class="btn" style="left:433px;top:274px;width:134px;height:30px;line-height:30px;font-size:12px">Know More</div>
</section>

<!-- NEWS -->
<section>
  <h2 class="section-title" style="top:2088px"><span class="hl">LATEST</span> NEWS</h2>
  <p class="intro" style="top:2150px">Stay up to date with everything happening at the club. Here you will find match reports, training updates, tournament dates and stories about our players. We post new articles every week during the season, so check back often and share the news with friends and family.<br>Upcoming camps and holiday sessions are listed here as soon as they are confirmed.</p>
  <div class="news-band" role="img" aria-label="Ice rink background"></div>
  <div class="news-img" style="left:47px" role="img" aria-label="Players competing for the puck"></div>
  <article class="news-card" style="left:326px">
    <div class="date">January 6th, 2017</div>
    <h3>Neque porro quisquam est</h3>
    <p>Our under twelve squad travelled north for a weekend cup and came home with silver medals and big smiles.</p>
    <div class="more">Read More &gt;&gt;</div>
  </article>
  <div class="news-img" style="left:618px" role="img" aria-label="Player lining up a shot"></div>
  <article class="news-card" style="left:897px">
    <div class="date">April 10th, 2017</div>
    <h3>Neque porro quisquam est</h3>
    <p>Spring training starts soon with new drills, extra ice time and a special goalie clinic for all ages.</p>
    <div class="more">Read More &gt;&gt;</div>
  </article>
  <div class="btn" style="left:561px;top:2554px;width:78px;height:26px;line-height:26px;font-size:11px">Know More</div>
</section>

<!-- TEAM -->
<section>
  <h2 class="section-title" style="top:2714px"><span class="hl">OUR</span> TEAM</h2>
  <p class="intro" style="top:2772px">Meet the young athletes who wear our colours with pride. Each player brings energy, courage and a love for the game. Our coaches help them grow as skaters and as teammates, and every match is a chance to learn something new together.<br>Click on a player to read their profile and season stats.</p>
  <div class="team-band" role="img" aria-label="Arena background"></div>
  <div class="player" style="left:91px;width:221px" role="img" aria-label="Player 1 portrait"><span class="num">07</span></div>
  <div class="player" style="left:360px;width:225px" role="img" aria-label="Player 2 portrait"><span class="num">21</span></div>
  <div class="player" style="left:628px;width:225px" role="img" aria-label="Player 3 portrait"><span class="num">22</span></div>
  <div class="player" style="left:897px;width:212px" role="img" aria-label="Player 4 portrait"><span class="num">36</span></div>
  <div class="player-name" style="left:91px;width:221px">Player 1</div>
  <div class="player-name" style="left:360px;width:225px">Player 2</div>
  <div class="player-name" style="left:628px;width:225px">Player 3</div>
  <div class="player-name" style="left:897px;width:212px">Player 4</div>
  <div class="btn" style="left:577px;top:3210px;width:76px;height:24px;line-height:24px;font-size:11px">More Info</div>
</section>

<!-- SHOP -->
<section>
  <h2 class="section-title" style="top:3402px"><span class="hl">FUN</span> SHOP</h2>
  <p class="intro" style="top:3474px">Show your support with official club jerseys, training gear and fan items for the whole family.<br>Orders are collected at the rink, and every purchase helps fund equipment for our youth teams.</p>
  <div class="shop-band" role="img" aria-label="Dark arena background"></div>
  <div class="promo">Save 20% off for all new Orders...HURRY !!!!</div>
  <div class="product" style="left:17px"><div class="jersey" role="img" aria-label="Black home jersey"></div><div class="strip"></div><span class="price">Price</span><span class="buy">Buy</span></div>
  <div class="product" style="left:249px"><div class="jersey light" role="img" aria-label="White away jersey"></div><div class="strip"></div><span class="price">Price</span><span class="buy">Buy</span></div>
  <div class="product" style="left:477px"><div class="jersey" role="img" aria-label="Black home jersey"></div><div class="strip"></div><span class="price">Price</span><span class="buy">Buy</span></div>
  <div class="product" style="left:706px"><div class="jersey light" role="img" aria-label="White away jersey"></div><div class="strip"></div><span class="price">Price</span><span class="buy">Buy</span></div>
  <div class="product" style="left:934px"><div class="jersey" role="img" aria-label="Black home jersey"></div><div class="strip"></div><span class="price">Price</span><span class="buy">Buy</span></div>
  <div class="product" style="left:1163px"><div class="jersey light" role="img" aria-label="White away jersey"></div><div class="strip"></div></div>
  <div class="btn" style="left:535px;top:3974px;width:80px;height:22px;line-height:22px;font-size:11px">View More</div>
</section>

<!-- CONTACT -->
<section>
  <div class="map" role="img" aria-label="Map showing the club location"></div>
  <div class="pin-label" style="left:446px;top:4244px"><i></i>Phone No</div>
  <div class="pin-label" style="left:378px;top:4288px"><i></i>Email Address</div>
  <div class="pin-label" style="left:260px;top:4332px;width:260px"><i></i>Our Proper Location</div>
  <div class="contact-side"></div>
  <h2 class="abs" style="left:690px;width:510px;top:4104px;text-align:center;font-size:18px;font-weight:400;color:#222;letter-spacing:1px">GET IN TOUCH</h2>
  <div class="field" style="top:4190px;height:50px">Name</div>
  <div class="field" style="top:4284px;height:50px">Email</div>
  <div class="field" style="top:4385px;height:135px">Address</div>
  <div class="btn" style="left:1018px;top:4486px;width:108px;height:34px;line-height:34px">SEND</div>
</section>

<!-- FOOTER -->
<footer class="footer">
  <svg class="abs" style="left:50px;top:44px" width="36" height="36"><circle cx="18" cy="18" r="16" fill="#f5c518"/></svg>
  <div class="abs serif" style="left:96px;top:36px;font-size:40px;font-weight:700;color:var(--gold)">Stags</div>
  <p class="abs" style="left:30px;top:190px;width:400px;font-size:12px;line-height:18px;color:var(--white)">Youth hockey for every child who loves the game.<br>Training, friendship and fair play all season long.<br>Join us at the rink and become part of the family.<br>Follow our news and events online every week.</p>
  <div class="social"><i></i><i></i><i></i><i></i><i></i><i></i><i></i><i></i></div>
  <div class="abs" style="left:676px;top:184px;font-size:14px;color:var(--white);letter-spacing:1px">NEWSLETTER</div>
  <div class="abs" style="left:676px;top:226px;width:484px;height:34px;background:#111"></div>
  <div class="abs" style="left:690px;top:235px;font-size:11px;color:#bbb">Enter your email id</div>
  <svg class="abs" style="left:950px;top:226px" width="210" height="34"><polygon points="30,0 210,0 210,34 0,34" fill="#f5c518"/></svg>
  <div class="abs" style="left:1040px;top:236px;font-size:11px;color:#222">SUBSCRIBE</div>
  <div class="bottom-bar">
    <nav class="bottom-nav"><a>HOME</a><a>NEWS</a><a>TEAM</a><a>CLUB</a><a>PARTNER</a><a>SHOP</a><a>CONTACT</a></nav>
    <div class="abs" style="right:50px;top:30px;font-size:11px;color:#ccc">Copyright 2017 Youth Hockey Club. All rights reserved</div>
  </div>
</footer>

</body>
</html>
```